Business Card Design

Lotside Ledger is an online automotive resource on a national scale specifically targeting lease purchases for new cars. Our Online and app platform allow prospective lease clients to scan a window sticker while at a franchise dealership and instantly receive a lease quote at what we call the sweet spot. Lotside Ledger offers price transparency during the lease process to allow average people the confidence in the lease process and takes away any fear of the big franchise dealers.
Lotside ledger allows ordinary lease customers to know they are getting a low price lease and not overpaying. Never overpay again

Industry/Entity Type

Automotive

Contact Information for Business Card

Lotside Ledger
Marcus Todwell (President of operations)
Phone: 888-302-7716
Cell: 561-448-2053

```html
<!DOCTYPE html>
<html lang="en">
<head>
<meta charset="utf-8">
<title>Lotside Ledger – Business Card</title>
<link rel="stylesheet" href="https://fonts.googleapis.com/css2?family=Source+Sans+3:wght@400;700&display=swap">
<style>
  :root {
    --backdrop: #b9b9bb;
    --card-black: #050505;
    --card-white: #ffffff;
    --ink-dark: #111111;
    --ink-light: #ffffff;
  }
  html, body {
    margin: 0;
    padding: 0;
    overflow: hidden;
  }
  .canvas {
    position: relative;
    width: 1200px;
    height: 745px;
    background: var(--backdrop);
    overflow: hidden;
    font-family: "Source Sans 3", sans-serif;
  }
  .card {
    position: absolute;
    width: 560px;
    height: 320px;
    box-sizing: border-box;
    box-shadow: 0 6px 18px rgba(0,0,0,0.25);
  }
  .card--front {
    left: 60px;
    top: 55px;
    background: var(--card-black);
    color: var(--ink-light);
  }
  .card--back {
    left: 580px;
    top: 370px;
    background: var(--card-white);
    color: var(--ink-dark);
  }
  .wordmark {
    position: absolute;
    display: flex;
    align-items: center;
    gap: 14px;
  }
  .wordmark__dot {
    width: 34px;
    height: 34px;
    border-radius: 50%;
    background: currentColor;
    flex: none;
  }
  .wordmark__name {
    font-weight: 700;
    text-transform: uppercase;
    line-height: 0.92;
    letter-spacing: 0.5px;
  }
  .card--front .wordmark {
    left: 118px;
    top: 108px;
  }
  .card--front .wordmark__name {
    font-size: 46px;
  }
  .card--back .wordmark {
    left: 70px;
    top: 52px;
  }
  .card--back .wordmark__name {
    font-size: 50px;
  }
  .contact {
    position: absolute;
    left: 232px;
    top: 170px;
    font-weight: 400;
    line-height: 1.05;
  }
  .contact__name {
    font-size: 26px;
    margin: 0;
  }
  .contact__title {
    font-size: 21px;
    margin: 0 0 12px;
  }
  .contact__phone {
    font-size: 28px;
    margin: 0;
  }
</style>
</head>
<body>
  <div class="canvas">
    <section class="card card--front" aria-label="Card front">
      <div class="wordmark">
        <span class="wordmark__dot"></span>
        <span class="wordmark__name">Lotside<br>Ledger</span>
      </div>
    </section>

    <section class="card card--back" aria-label="Card back">
      <div class="wordmark">
        <span class="wordmark__dot"></span>
        <span class="wordmark__name">Lotside<br>Ledger</span>
      </div>
      <div class="contact">
        <p class="contact__name">Marcus Todwell</p>
        <p class="contact__title">President of operations</p>
        <p class="contact__phone">888-302-7716</p>
        <p class="contact__phone">561-448-2053</p>
      </div>
    </section>
  </div>
</body>
</html>
```